Eco conscious print and frame company needs a website

‘LUMAeco is a new company that makes frames and fine art prints from sustainable bamboo. Our site should have an organic feel yet still have a professional clean look to it as well.
We need shopping cart and image uploading capabilities much like a pictorama or glowbird type of site only on a much smaller scale.
Currently we have 3 different styles available in sizes from 8"x8" all the way to 4ft by 8ft.
Target audience will be the snapvintra, pixelgram, zephone market.

Target Market(s)

20-40 years old male and female. Pixelgram generation.

Industry/Entity Type

Shopping

Requirements
Must have
• Front end and back end capabilities with emphasis on image uploading and shopping cart functionality.

```html
<!DOCTYPE html>
<html lang="en">
<head>
<meta charset="utf-8">
<title>LUMAeco – Frames and Fine Art Prints</title>
<link rel="stylesheet" href="https://fonts.googleapis.com/css2?family=Nunito:wght@600;700;800&family=Arimo:wght@400&display=swap">
<style>
  :root {
    --wood-light: #e9c9a3;
    --wood-mid: #dcb58a;
    --lime: #c4e35a;
    --lime-deep: #a9d232;
    --panel-top: #e3eedb;
    --panel-white: #ffffff;
    --green-text: #3e7d10;
    --green-dark: #2f6a0a;
    --nav-grey: #4f4f4f;
    --body-grey: #666666;
    --orange-light: #fbbe55;
    --orange: #f7941d;
    --bullet-gold: #f4d24b;
    --frame-wood: #ecc9a6;
    --frame-edge: #d7a77d;
  }
  * { box-sizing: border-box; margin: 0; padding: 0; }
  html, body { width: 1200px; height: 672px; overflow: hidden; }
  body {
    position: relative;
    font-family: "Arimo", Arial, sans-serif;
    background: linear-gradient(90deg, var(--wood-light), var(--wood-mid) 30%, var(--wood-light) 55%, var(--wood-mid) 80%, var(--wood-light));
  }
  .hero-band {
    position: absolute; left: 0; top: 59px; width: 1200px; height: 368px;
    background: radial-gradient(ellipse at 50% 40%, var(--lime-deep), var(--lime) 60%);
    border-top: 1px solid #e4f3a6; border-bottom: 1px solid #e4f3a6;
  }
  .fold { position: absolute; }
  .header-panel {
    position: absolute; left: 150px; top: 11px; width: 900px; height: 102px;
    background: linear-gradient(180deg, var(--panel-top), var(--panel-white));
    box-shadow: 0 3px 8px rgba(60,100,0,.25);
  }
  .brand {
    position: absolute; left: 40px; top: 56px;
    font-family: "Nunito", sans-serif; font-weight: 700; font-size: 26px;
    color: var(--green-dark); display: flex; align-items: center; gap: 8px;
  }
  .brand-dot { width: 14px; height: 14px; border-radius: 50%; background: var(--green-text); }
  .account-links {
    position: absolute; right: 52px; top: 12px;
    font-family: "Nunito", sans-serif; font-weight: 600; font-size: 18px; color: var(--green-text);
    display: flex; gap: 24px;
  }
  .account-links .sep { color: #555; }
  .main-nav {
    position: absolute; right: 52px; top: 59px;
    display: flex; gap: 50px;
    font-family: "Nunito", sans-serif; font-weight: 600; font-size: 18px; color: var(--nav-grey);
  }
  .main-nav .current { color: var(--green-text); }
  .hero-copy { position: absolute; left: 191px; top: 134px; }
  .hero-title {
    font-family: "Nunito", sans-serif; font-weight: 800; font-size: 32px; line-height: 39px;
    color: #fbfde9; text-shadow: 0 2px 3px rgba(50,90,0,.45);
  }
  .hero-title .accent { color: var(--bullet-gold); }
  .feature-list { list-style: none; margin-top: 16px; }
  .feature-list li {
    font-size: 15.5px; color: var(--green-dark); line-height: 24.5px;
    display: flex; align-items: center; gap: 8px;
  }
  .upload-button {
    display: inline-block; margin-top: 20px; width: 164px; height: 42px;
    border-radius: 4px; text-align: center; line-height: 42px;
    font-family: "Nunito", sans-serif; font-weight: 800; font-size: 17px; color: #fff;
    text-shadow: 0 1px 2px rgba(150,60,0,.6);
    background: linear-gradient(180deg, var(--orange-light), var(--orange));
    box-shadow: 0 2px 4px rgba(80,80,0,.4);
  }
  .hero-art { position: absolute; left: 520px; top: 128px; }
  .steps-panel {
    position: absolute; left: 150px; top: 384px; width: 900px; height: 232px;
    background: linear-gradient(180deg, var(--panel-top), var(--panel-white) 45%);
  }
  .step { position: absolute; top: 33px; }
  .step-icon { position: absolute; top: 0; border-radius: 4px; }
  .step-title {
    position: absolute; top: 29px; width: 170px;
    font-family: "Nunito", sans-serif; font-weight: 600; font-size: 16px; line-height: 19px; color: var(--green-text);
  }
  .step-text {
    position: absolute; top: 89px; width: 260px;
    font-size: 12.5px; line-height: 22.5px; color: var(--body-grey);
  }
  .site-footer {
    position: absolute; left: 0; top: 615px; width: 1200px; height: 57px;
    background: linear-gradient(180deg, var(--orange-light), var(--orange));
    border-top: 1px solid #e08a1a;
  }
  .copyright { position: absolute; left: 189px; top: 18px; font-size: 12px; color: #fff; }
</style>
</head>
<body>
  <div class="hero-band"></div>

  <svg class="fold" style="left:132px;top:29px" width="20" height="88" viewBox="0 0 20 88"><polygon points="18,0 0,2 10,88 18,88" fill="#d2e4c6"/></svg>
  <svg class="fold" style="left:1049px;top:29px" width="20" height="88" viewBox="0 0 20 88"><polygon points="2,0 20,2 10,88 2,88" fill="#d2e4c6"/></svg>
  <svg class="fold" style="left:132px;top:384px" width="20" height="84" viewBox="0 0 20 84"><polygon points="18,0 10,0 0,82 18,84" fill="#d2e4c6"/></svg>
  <svg class="fold" style="left:1049px;top:384px" width="20" height="84" viewBox="0 0 20 84"><polygon points="2,0 10,0 20,82 2,84" fill="#d2e4c6"/></svg>

  <header class="header-panel">
    <div class="brand"><span class="brand-dot"></span>LUMAeco</div>
    <div class="account-links"><span>Sign Up</span><span class="sep">|</span><span>Login</span></div>
    <nav class="main-nav">
      <span class="current">Home</span><span>Products</span><span>Gallery</span><span>About Us</span><span>Contact</span>
    </nav>
  </header>

  <section class="hero-copy">
    <h1 class="hero-title">Create FREE Fine Art Print<br><span class="accent">or</span> Try our Premium Product</h1>
    <ul class="feature-list">
      <li><svg width="14" height="10" viewBox="0 0 14 10"><polyline points="1,5 5,9 13,1" fill="none" stroke="var(--bullet-gold)" stroke-width="2"/></svg>Simply upload photos.</li>
      <li><svg width="14" height="10" viewBox="0 0 14 10"><polyline points="1,5 5,9 13,1" fill="none" stroke="var(--bullet-gold)" stroke-width="2"/></svg>Choose the variety of frames.</li>
      <li><svg width="14" height="10" viewBox="0 0 14 10"><polyline points="1,5 5,9 13,1" fill="none" stroke="var(--bullet-gold)" stroke-width="2"/></svg>Print your chosen design</li>
    </ul>
    <span class="upload-button">Upload Photo</span>
  </section>

  <svg class="hero-art" width="490" height="256" viewBox="0 0 490 256" role="img" aria-label="Two tilted bamboo frames holding vintage beach photographs">
    <defs>
      <linearGradient id="frameTone" x1="0" y1="0" x2="1" y2="1">
        <stop offset="0" stop-color="#f3dbc0"/><stop offset="1" stop-color="#d9ab80"/>
      </linearGradient>
      <linearGradient id="printTone" x1="0" y1="0" x2="1" y2="1">
        <stop offset="0" stop-color="#8a8c6a"/><stop offset="1" stop-color="#6f7a3e"/>
      </linearGradient>
    </defs>
    <polygon points="10,162 95,136 126,256 26,256" fill="url(#frameTone)"/>
    <polygon points="92,94 421,4 488,256 135,256" fill="url(#frameTone)"/>
    <polygon points="120,108 400,34 455,256 155,256" fill="url(#printTone)"/>
  </svg>

  <section class="steps-panel">
    <div class="step" style="left:42px">
      <div class="step-icon" style="left:0;width:73px;height:71px;background:linear-gradient(160deg,#e98a2c,#9ba0a8)" role="img" aria-label="Camera with photo icon"></div>
      <h2 class="step-title" style="left:99px">Upload your photos and adjust it</h2>
      <p class="step-text" style="left:-2px">Lorem ipsum dolor sit amet, consectetur adipiscing elit. Etiam auctor tortor tellus, ut consectetur arcu.</p>
    </div>
    <div class="step" style="left:333px">
      <div class="step-icon" style="left:0;width:58px;height:68px;background:linear-gradient(160deg,#c0772e,#8fc66a)" role="img" aria-label="Framed picture icon"></div>
      <h2 class="step-title" style="left:72px">Choose frames and customize it</h2>
      <p class="step-text" style="left:-2px">Lorem ipsum dolor sit amet, consectetur adipiscing elit. Etiam auctor tortor tellus, ut consectetur arcu.</p>
    </div>
    <div class="step" style="left:626px">
      <div class="step-icon" style="left:0;width:91px;height:68px;background:linear-gradient(180deg,#e4e6e8,#6b6d70)" role="img" aria-label="Printer icon"></div>
      <h2 class="step-title" style="left:107px">Purchase and print your design</h2>
      <p class="step-text" style="left:-2px">Lorem ipsum dolor sit amet, consectetur adipiscing elit. Etiam auctor tortor tellus, ut consectetur arcu.</p>
    </div>
  </section>

  <footer class="site-footer">
    <p class="copyright">Copyright (c) lumaeco.com 2012. All rights reserved.</p>
  </footer>
</body>
</html>
```